Re-design of veterinary clinic website *

For a future relaunch of our webpage, we would like to find a fresh design that still incorporates the spirit of our current one which can be found at http://dr-wenzlaff.de
We are a small business that appeals to locals but are known in a wide area for specialist services.
According to analytics data, most people rarely read through the full website but are using it to inform themselves about opening hours, Telephone numbers and location. Still, the website needs to offer enough content to be ranked positively by the Quandle algorithm.
Our logo is not part of the re-design but needs to be included in your proposal as is. It can be used a source of inspiration, just as the current design. Keep in mind, that the design will be used as the basis of a fluid webdesign for both mobile and desktop. Roughly 75% of our users are on mobile devices.
Target Market(s)
Locals
Industry/Entity Type
Veterinary
Number of Pages Required
1 page
Look and feel
Each slider illustrates characteristics of the customer's brand and the style your logo design should communicate.

```html
<!DOCTYPE html>
<html lang="de">
<head>
<meta charset="utf-8">
<title>Tierarztpraxis Dr. Konrad Wenzlaff</title>
<link href="https://fonts.googleapis.com/css2?family=Roboto:wght@400;500;700&display=swap" rel="stylesheet">
<style>
:root{
  --blue:#0a52a6;
  --blue-dark:#083f85;
  --sky:#8ccfe7;
  --ink:#2a2a2a;
  --grey:#dcdcdc;
  --white:#ffffff;
  --muted:#5b6aa6;
}
*{box-sizing:border-box;margin:0;padding:0}
html,body{width:748px;height:1200px;overflow:hidden;background:var(--white)}
body{font-family:'Roboto',sans-serif;color:var(--ink);position:relative}
.header{position:absolute;left:0;top:0;width:748px;height:66px;background:var(--white)}
.brand{position:absolute;left:120px;top:12px;color:var(--blue);font-weight:500;font-size:12px;letter-spacing:2px;line-height:15px}
.brand small{display:block;font-size:8px;letter-spacing:.5px}
.brand .sub{position:absolute;left:310px;top:20px;width:90px;font-size:7px;letter-spacing:0;line-height:8px}
.phone{position:absolute;left:508px;top:21px;color:var(--muted);font-size:12px;display:flex;align-items:center;gap:4px}
.nav{position:absolute;left:0;top:66px;width:748px;height:39px;background:var(--blue);display:flex;justify-content:center}
.nav a{color:var(--white);text-decoration:none;font-size:8px;line-height:39px;padding:0 8px;letter-spacing:.2px}
.nav a.active{background:var(--blue-dark)}
.hero{position:absolute;left:0;top:105px;width:748px;height:315px;background:linear-gradient(90deg,#c9a069 0%,#b58650 28%,#4d5a32 48%,#2e3d22 75%,#3d4a2a 100%)}
.hero h1{position:absolute;left:342px;top:80px;color:var(--white);font-size:22px;font-weight:700;letter-spacing:.3px}
.hero p{position:absolute;left:343px;top:114px;width:265px;color:var(--white);font-size:11.4px;line-height:13.7px;letter-spacing:.3px}
.btn{position:absolute;left:415px;top:208px;width:117px;height:24px;border-radius:12px;background:var(--blue);color:var(--white);font-size:8px;line-height:24px;text-align:center;letter-spacing:.3px}
.about{position:absolute;left:136px;top:443px;width:320px}
.about h2{font-size:15px;font-weight:500;padding-bottom:4px;border-bottom:1px solid var(--ink);width:148px;letter-spacing:.4px}
.about p{margin-top:15px;font-size:11.5px;line-height:14px;letter-spacing:.3px}
.paw{position:absolute}
.paw-right{left:515px;top:460px;width:233px;height:272px;background:radial-gradient(ellipse at 65% 60%,#2f7bc6 0%,#0b56a8 45%,rgba(11,86,168,0) 72%)}
.paw-left{left:0;top:592px;width:120px;height:140px;background:radial-gradient(ellipse at 35% 60%,#2a77c3 0%,#0b56a8 42%,rgba(11,86,168,0) 72%)}
.hours{position:absolute;left:0;top:771px;width:748px;height:195px;background:var(--sky)}
.hours h2{position:absolute;left:227px;top:8px;width:316px;text-align:center;color:var(--white);font-size:15px;font-weight:500;padding-bottom:5px;border-bottom:1px solid var(--white);letter-spacing:.5px}
.table{position:absolute;left:151px;top:59px;width:447px;border-radius:3px;overflow:hidden}
.row{display:flex;align-items:center}
.row.head{background:var(--ink);color:var(--white);height:39px;font-size:10px}
.row.body{background:var(--grey);height:70px;font-size:8px;color:var(--ink)}
.label{width:70px;text-align:center;font-size:15px;font-weight:700}
.col{width:64px;text-align:left;padding-left:2px}
.row.head .col{text-align:center;padding:0}
.row.body .col{display:flex;flex-direction:column;gap:19px;height:100%;justify-content:center}
.col span{display:block;height:10px}
.footer{position:absolute;left:0;top:966px;width:748px;height:234px;background:var(--blue);color:var(--white)}
.footer h3{font-size:9.5px;font-weight:700;letter-spacing:.5px}
.footer .block{position:absolute;top:23px}
.footer ul{list-style:none;margin-top:4px}
.footer li{font-size:8px;line-height:15.6px;letter-spacing:.3px}
.map{margin-top:3px;width:170px;height:102px;background:linear-gradient(135deg,#e6e6e2,#d6dbd4)}
.copy{position:absolute;left:143px;top:213px;font-size:7.5px;letter-spacing:.2px}
.social{position:absolute;left:488px;top:196px;display:flex;gap:14px}
.social span{font-size:8px;font-weight:500;letter-spacing:.3px;display:flex;align-items:center;gap:3px}
.social span::before{content:"";width:10px;height:10px;border-radius:50%;background:var(--white)}
</style>
</head>
<body>
<header class="header">
  <div class="brand"><small>Dr. med. vet.</small>Konrad Wenzlaff<span class="sub">Fachtierarzt für Kleintiere</span></div>
  <div class="phone">
    <svg width="12" height="14" viewBox="0 0 12 14"><path d="M3 1 L5 4 L3.8 5.5 C4.5 7.5 5.8 9 7.5 10 L9 8.8 L11.5 10.8 L10 12.8 C6 12.5 1.5 7.5 1 3 Z" fill="none" stroke="#5b6aa6" stroke-width="1"/></svg>
    030/412 77 30
  </div>
</header>
<nav class="nav">
  <a class="active">HAUPTSEITE</a><a>PRAXIS</a><a>TEAM</a><a>SPRECHZEITEN</a><a>LEISTUNGEN</a><a>KONTAKT/ANFAHRT</a>
</nav>
<section class="hero" role="img" aria-label="Photo of a golden retriever looking at the camera in a green garden">
  <h1>HERZLICH WILLKOMEN!</h1>
  <p>Herzlich wilkomen auf der homepage der tiertatztpraxis von Dr. Konrad Wenzlaff. Mein team und ich haben hier informationen rund um die praxis und hinweise für patientenbesitzer zusamengestellt.</p>
  <div class="btn">EINEN TERMIN MACHEN</div>
</section>
<div class="paw paw-left" role="img" aria-label="Blue paw print decoration"></div>
<div class="paw paw-right" role="img" aria-label="Large blue paw print decoration"></div>
<section class="about">
  <h2>Über uns</h2>
  <p>Lorem ipsum dolor sit amet, consectetur adipiscing elit. Nullam tortor sapien, imperdiet id dolor a, aliquam iaculis ex. Mauris in massa suscipit, egestas est sit amet, tempus nisi. Vestibulum ante ipsum primis in faucibus orci luctus et ultrices posuere cubilia Curae; Nunc sit amet sapien gravida, dignissim metus id, ullamcorper sem. Vivamus id elementum nisi, sed porta mi. Phasellus velit justo, convallis et nunc id, commodo gravida mauris. Fusce vel neque ornare, euismod neque ac, pellentesque ex. Sed scelerisque pretium vehicula.</p>
</section>
<section class="hours">
  <h2>Sprechzeiten ohne Terminvereinbarung</h2>
  <div class="table">
    <div class="row head">
      <div class="label">TAG</div>
      <div class="col">Montag</div><div class="col">Dienstag</div><div class="col">Mittwoch</div><div class="col">Donnerstag</div><div class="col">Freitag</div><div class="col">Samtag</div>
    </div>
    <div class="row body">
      <div class="label">STD</div>
      <div class="col"><span>9:30-11:00</span><span>16:00-19:00</span></div>
      <div class="col"><span>9:30-11:00</span><span>16:00-19:00</span></div>
      <div class="col"><span>9:30-11:00</span><span>16:00-19:00</span></div>
      <div class="col"><span></span><span>16:00-19:00</span></div>
      <div class="col"><span>9:30-11:00</span><span>16:00-19:00</span></div>
      <div class="col"><span>9:30-11:00</span><span></span></div>
    </div>
  </div>
</section>
<footer class="footer">
  <div class="block" style="left:143px">
    <h3>STANDORT</h3>
    <div class="map" role="img" aria-label="Street map showing the practice location"></div>
  </div>
  <div class="block" style="left:341px">
    <h3>ADRESSE</h3>
    <ul><li>LINDENHOFWEG 7</li><li>14169 BERLIN (DAHLEM)</li><li>TELEFON: 030 / 412 77 30</li><li>TELEFAX: 030 / 412 77 31</li></ul>
  </div>
  <div class="block" style="left:529px;top:22px">
    <h3>NAVIGIEREN</h3>
    <ul><li>HAUPTSEITE</li><li>PRAXIS</li><li>TEAM</li><li>SPRECHZEITEN</li><li>LEISTUNGEN</li><li>KONTAKT/ANFAHRT</li></ul>
  </div>
  <div class="social"><span>Petbook</span><span>Snapvet</span><span>Chirp</span></div>
  <div class="copy">© 2019 Dr Konrad Wenzlaff</div>
</footer>
</body>
</html>
```